Harrowby Wine Label - Design a front and smaller back label for an exclusive red wine

Harrowby Wines produces a very high quality, high priced wine from an old and prestigous vineyard in one of Australia's oldest, but smallest wine growing regions. The grapevines are old (like old men with gnarled arms and trunks) and they produce fewer grapes than younger vines but the grape quality (and thus wine quality) is magnificent and highly sought after as it produces wine of exceptional quality.
The vineyard was purchased by the Harrowby family in February 2010 from a multinational wine company who made wonderful, trophy winning wines for 10 years before the vineyard went into a decline.
The challenge is to produce 2 labels - a simple main front label that focuses on the Harrowby brand and a smaller, information rich, back label that relates the history of the vineyard.
The labels should have a white or charcoal grey background and impart tradition, quality, exclusivity and a little self indulgence which is why we want the family crest incorporated - the choice of font will help.
It might also impart a sense of fun so that it appeals to the 25-35 year old age bracket.
The label should be kept clean and simple not loud and busy. Preferred colours are black, grey and white. Red is fine if used sparingly

Here are the details:_

Front Label (115 long x 65-90mm wide)

Harrowby
Lanternwatch Reserve
2011
Mudgee
Wine of Australia 750ml

Back Label (dimensions to suit text and front label design; font size small; text in black so that it is readable in less than optimal light (eg candlelight at a restaurant table).

Harrowby
Lanternwatch Reserve 2011

This is the first release of The Lanternwatch’s Reserve – just 100 dozen bottles were made. The wine was made from Shiraz and 10% Cabernet Sauvignon grapes sourced from an iconic Mudgee vineyard that was established 1966 by Peter Vallis. In 1994, the vineyard known as ”Silver Hollow”, became the source of a decade of formidable, trophy winning wines under Tindalberg’s and later Quellwood’s ownership. The 20ha vineyard was purchased by Corin & Margaret Harrowby in 2010. The Silver Hollow name was retained by Quellwoods; no wine has been released under this label since the 2006 vintage.

The shaky old Shiraz vines are slowly being restored to full health using careful cane pruning techniques that stimulates fresh, new tissue growth, more even bunch sizes and better grape quality and consistency. The Shiraz grapes used in this wine were hand-picked from two rows of the first crop from the 46 year old, cane pruned vines. The 2011 Reserve is the first step to re-establish the traditions of a famous vineyard and one of Australia’s most sought after export wines.

“Deep and intense purple hues with aromas of ripe blackberry fruits, spice and eucalypt with rich chocolate complemented by subtle oak overtones. A rich and full bodied wine exhibiting a soft yet generous palate with plum, forest fruits and mint chocolate notes. A fine grained tannin structure displaying integrated oak characters adds to the complexity of the wine. This wine was aged for 18 months in a blend of new French oak hogsheads and one year old American hogsheads, crafting a blend with great structure and length of flavour which will develop into a Mudgee classic” – Lewis Farrant, Winemaker

13.5% Alc/Vol.
Contains approx 8.0 std drinks
Preservative (220) added

Harrowby Wines
Tallowbend Rd, Mudgee 2850
www.harrowbywines.example.au

Reason: My apologies to the designers who have kindly submitted some wonderful designs. I am trying to achieve a conscentious between shareholders. This is difficult as they are in different parts of the world and I have learned through this experience that opinions on wine labels are quite diverse!!! The feedback I have received so far indicates the following (1) A light or white background is preferred (2) The crest should not be a dominant part of the label (3) The label needs to be clean, fresh and uncomplicated (4) If red is used it should be in minor detail only (5) "Harrowby" should be distinctive. The font is difficult for us! (6) We are considering "The Lanternwatch" RESERVE instead of "Lanternwatch's" RESERVE (7) The text on the back label is too long; I will edit and re-upload Many thanks for your help and patience Kind regards Corin

Good Morning All,
I have edited the back label text to reduce the size of the label. A Word file with the changes has just been uploaded.
Cheers
Corin

Dear Designers,
Thank you all so very much for the wonderful selection of designs you have submitted my family have all been overwhelmed by the quality and skill level exhibited and we all appreciate you your efforts
Kindest regards
Corin

Target Market(s)

25-35 year old men and women of Australia, China, US & UK

Industry/Entity Type

Restaurant

Requirements
Must have
• Crest
Should not have
• Animals on the label

```html
<!DOCTYPE html>
<html lang="en">
<head>
<meta charset="utf-8">
<title>Harrowby Wines – The Lanternwatch Reserve 2011</title>
<link rel="stylesheet" href="https://fonts.googleapis.com/css2?family=Cinzel:wght@400;500&family=Cormorant+Garamond:wght@400;500&family=Pinyon+Script&display=swap">
<style>
  :root {
    --paper: #ffffff;
    --ink: #111111;
    --ink-soft: #2a2a2a;
    --crest-grey: #cfcfcf;
    --crest-grey-light: #e6e6e6;
    --gate-grey: #d4d4d4;
    --reserve-red: #c0151f;
  }
  html, body {
    margin: 0;
    padding: 0;
    width: 845px;
    height: 1200px;
    overflow: hidden;
    background: var(--paper);
  }
  .label {
    position: relative;
    width: 845px;
    height: 1200px;
    background: var(--paper);
    color: var(--ink);
  }
  .label > * { position: absolute; margin: 0; }

  .est {
    top: 124px;
    font-family: "Cinzel", serif;
    font-size: 17px;
    letter-spacing: 1px;
    color: var(--ink-soft);
  }
  .est--word { left: 287px; }
  .est--year { left: 491px; }

  .crest {
    left: 364px;
    top: 68px;
    width: 100px;
    height: 188px;
  }

  .brand {
    left: 0;
    width: 845px;
    top: 388px;
    text-align: center;
    font-family: "Cinzel", serif;
    font-weight: 400;
    font-size: 58px;
    letter-spacing: 6px;
    line-height: 1;
    color: var(--ink);
  }
  .brand-sub {
    left: 0;
    width: 845px;
    top: 478px;
    text-align: center;
    font-family: "Cinzel", serif;
    font-size: 18px;
    letter-spacing: 17px;
    text-indent: 17px;
    color: var(--ink);
  }

  .wine-name {
    left: 222px;
    top: 648px;
    width: 400px;
    text-align: center;
    font-family: "Pinyon Script", cursive;
    font-size: 46px;
    line-height: 1;
    transform: rotate(-20deg);
    color: var(--ink);
  }

  .gates {
    left: 314px;
    top: 779px;
    width: 204px;
    height: 70px;
  }

  .reserve {
    left: 0;
    width: 845px;
    top: 856px;
    text-align: center;
    font-family: "Cormorant Garamond", serif;
    font-weight: 500;
    font-size: 35px;
    letter-spacing: 5px;
    text-indent: 5px;
    line-height: 1;
    color: var(--reserve-red);
  }
  .vintage {
    left: 0;
    width: 845px;
    top: 905px;
    text-align: center;
    font-family: "Pinyon Script", cursive;
    font-size: 30px;
    line-height: 1;
    color: var(--ink);
  }

  .details {
    left: 0;
    width: 845px;
    top: 1018px;
    text-align: center;
    font-family: "Cormorant Garamond", serif;
    color: var(--ink);
    line-height: 1;
  }
  .details p { margin: 0; }
  .details .volume { font-size: 19px; font-weight: 500; }
  .details .region { font-size: 33px; letter-spacing: 2px; margin-top: 7px; }
  .details .origin { font-size: 21px; letter-spacing: 1px; margin-top: 5px; }
</style>
</head>
<body>
  <main class="label">
    <span class="est est--word">EST.</span>
    <svg class="crest" viewBox="0 0 100 188" role="img" aria-label="Harrowby family crest in soft grey">
      <defs>
        <linearGradient id="crestTone" x1="0" y1="0" x2="0" y2="1">
          <stop offset="0" stop-color="var(--crest-grey-light)"/>
          <stop offset="1" stop-color="var(--crest-grey)"/>
        </linearGradient>
      </defs>
      <rect x="0" y="0" width="100" height="188" fill="url(#crestTone)"/>
    </svg>
    <span class="est est--year">2010</span>

    <h1 class="brand">HARROWBY</h1>
    <p class="brand-sub">WINES</p>

    <h2 class="wine-name">The Lanternwatch</h2>

    <svg class="gates" viewBox="0 0 204 70" role="img" aria-label="Pair of grey farm gate emblems">
      <rect x="0" y="0" width="100" height="70" fill="var(--gate-grey)"/>
      <rect x="104" y="0" width="100" height="70" fill="var(--gate-grey)"/>
    </svg>

    <p class="reserve">RESERVE</p>
    <p class="vintage">2011</p>

    <div class="details">
      <p class="volume">750mL</p>
      <p class="region">MUDGEE</p>
      <p class="origin">WINE OF AUSTRALIA</p>
    </div>
  </main>
</body>
</html>
```